New finance and accounting services business needs banner ads

We need 3 web banner ads to use on local news websites. Our cool branding/logo (thank you Pixel Harbor!) will give you a great creative start to bring life to an otherwise dull service (that is the perception anyway).

Key ideas to be in the ads:
- We relieve stress for small business owners
- The cheapest way to get a CFO (Chief Financial Officer) is to 'rent' one part-time
- What will you do with all the cash we find you?

Target Market(s)

Small business owners (less than 50 employees) who are stressed out and don't like budgets, finance, or accounting

Industry/Entity Type

Professional Service

Font styles to use
Other font styles liked:
• Fonts which match our logo

Colors

Designer to choose colors to be used in the design.

Requirements
Must have
• - Multiple sizes/layouts to fit within various ad spaces.
• - Show a message of stress relief
• - Show a message of the business owner getting more money (which helps with stress)
• - Must use the logo prominently (we are introducing the company with these ads)
Nice to have
• Some light-hearted humor is always a nice touch

```html
<!DOCTYPE html>
<html lang="en">
<head>
<meta charset="utf-8">
<title>Clearview Ledger – Banner Set</title>
<link href="https://fonts.googleapis.com/css2?family=Bree+Serif&family=Passion+One:wght@400;700&family=Oswald:wght@400;500&family=Open+Sans:wght@700&display=swap" rel="stylesheet">
<style>
  :root {
    --stage-dark: #15181c;
    --stage-mid: #3a4047;
    --cream: #fcefd6;
    --tan: #b4915a;
    --tan-dark: #9c7a47;
    --slate: #2e3d48;
    --ink: #293843;
    --red: #c3171c;
    --red-dark: #8f0d10;
    --white: #ffffff;
    --gold: #f2b53c;
  }
  * { margin: 0; padding: 0; box-sizing: border-box; }
  html, body { width: 1200px; height: 685px; overflow: hidden; }
  body {
    position: relative;
    background: radial-gradient(ellipse at 70% 20%, var(--stage-mid), var(--stage-dark) 75%);
    font-family: "Passion One", sans-serif;
  }
  .banner {
    position: absolute;
    background: var(--cream);
    overflow: hidden;
    box-shadow: 0 4px 14px rgba(0,0,0,.45);
  }
  .banner > * { position: absolute; }
  .banner-band { left: 0; top: 0; width: 100%; height: 100%; }
  .brand-mark {
    border-radius: 50%;
    background: var(--slate);
  }
  .brand-name {
    font-family: "Bree Serif", serif;
    color: var(--ink);
    white-space: nowrap;
    line-height: 1;
    letter-spacing: .3px;
  }
  .brand-name.is-red { color: var(--red); }
  .headline {
    font-family: "Passion One", sans-serif;
    font-weight: 700;
    color: var(--ink);
    line-height: 1;
    letter-spacing: .6px;
    white-space: nowrap;
  }
  .subline {
    font-family: "Oswald", sans-serif;
    color: var(--ink);
    line-height: 1.05;
    text-align: center;
  }
  .subline-box {
    font-family: "Oswald", sans-serif;
    background: var(--slate);
    color: var(--white);
    display: flex; align-items: center; justify-content: center;
    white-space: nowrap;
  }
  .cta {
    font-family: "Open Sans", sans-serif;
    font-weight: 700;
    color: var(--white);
    background: linear-gradient(var(--red), var(--red-dark));
    border-radius: 7px;
    display: flex; align-items: center; justify-content: center;
    box-shadow: 0 2px 3px rgba(0,0,0,.35);
    white-space: nowrap;
  }
  .mascot {
    border-radius: 18px;
    background: linear-gradient(180deg, var(--slate) 0%, var(--slate) 50%, var(--gold) 100%);
  }
  .center { text-align: center; }
</style>
</head>
<body>

<!-- Skyscraper 120 -->
<div class="banner" style="left:66px;top:41px;width:121px;height:602px;">
  <svg class="banner-band" viewBox="0 0 121 602" preserveAspectRatio="none" aria-hidden="true">
    <polygon points="0,430 121,365 121,602 0,602" fill="var(--tan)"/>
  </svg>
  <div class="brand-mark" style="left:42px;top:27px;width:36px;height:36px;"></div>
  <div class="brand-name center" style="left:0;width:121px;top:72px;font-size:11.5px;">CLEARVIEW LEDGER</div>
  <div class="headline center" style="left:0;width:121px;top:151px;font-size:21px;">WHAT WILL</div>
  <div class="headline center" style="left:0;width:121px;top:165px;font-size:33px;">YOU DO</div>
  <div class="subline" style="left:0;width:121px;top:196px;font-size:13px;">WITH ALL THE CASH<br>WE FIND YOU?</div>
  <div class="mascot" role="img" aria-label="Cartoon finance mascot holding two bags of money" style="left:10px;top:315px;width:108px;height:168px;"></div>
  <div class="cta" style="left:18px;top:539px;width:88px;height:22px;font-size:10px;">LEARN MORE</div>
</div>

<!-- Skyscraper 160 -->
<div class="banner" style="left:214px;top:41px;width:161px;height:602px;">
  <svg class="banner-band" viewBox="0 0 161 602" preserveAspectRatio="none" aria-hidden="true">
    <polygon points="0,475 161,420 161,602 0,602" fill="var(--tan)"/>
  </svg>
  <div class="brand-mark" style="left:56px;top:21px;width:48px;height:48px;"></div>
  <div class="brand-name center" style="left:0;width:161px;top:81px;font-size:15px;">CLEARVIEW LEDGER</div>
  <div class="headline center" style="left:0;width:161px;top:162px;font-size:28px;">WHAT WILL</div>
  <div class="headline center" style="left:0;width:161px;top:181px;font-size:40px;">YOU DO</div>
  <div class="subline" style="left:0;width:161px;top:221px;font-size:17px;">WITH ALL THE CASH<br>WE FIND YOU?</div>
  <div class="mascot" role="img" aria-label="Cartoon finance mascot holding two bags of money" style="left:10px;top:291px;width:146px;height:224px;"></div>
  <div class="cta" style="left:22px;top:553px;width:116px;height:30px;font-size:13px;">LEARN MORE</div>
</div>

<!-- Leaderboard small -->
<div class="banner" style="left:401px;top:171px;width:490px;height:60px;">
  <svg class="banner-band" viewBox="0 0 490 60" preserveAspectRatio="none" aria-hidden="true">
    <polygon points="379,0 490,0 490,60 384,60 392,30" fill="var(--tan)"/>
    <polygon points="392,30 384,60 400,60" fill="var(--tan-dark)"/>
  </svg>
  <div class="brand-mark" style="left:43px;top:4px;width:32px;height:32px;"></div>
  <div class="brand-name is-red center" style="left:5px;width:100px;top:42px;font-size:10px;">CLEARVIEW LEDGER</div>
  <div class="headline" style="left:143px;top:6px;font-size:24px;letter-spacing:1.6px;">WHAT WILL YOU DO</div>
  <div class="subline-box" style="left:143px;top:30px;width:212px;height:20px;font-size:14px;">WITH ALL THE CASH WE FIND YOU?</div>
  <div class="cta" style="left:415px;top:22px;width:64px;height:16px;font-size:7.5px;border-radius:5px;">LEARN MORE</div>
</div>

<!-- Medium rectangle wide -->
<div class="banner" style="left:401px;top:251px;width:338px;height:281px;">
  <div class="brand-mark" style="left:43px;top:9px;width:40px;height:40px;"></div>
  <div class="brand-name" style="left:15px;top:57px;font-size:13.5px;">CLEARVIEW LEDGER</div>
  <div class="headline" style="left:15px;top:113px;font-size:36px;">WHAT WILL</div>
  <div class="headline" style="left:15px;top:139px;font-size:48px;">YOU DO</div>
  <div class="subline-box" style="left:15px;top:183px;width:168px;height:22px;font-size:13px;">WITH ALL THE CASH WE FIND YOU?</div>
  <div class="cta" style="left:79px;top:245px;width:106px;height:26px;font-size:12px;">LEARN MORE</div>
  <div class="mascot" role="img" aria-label="Cartoon finance mascot holding two bags of money" style="left:191px;top:49px;width:140px;height:220px;"></div>
</div>

<!-- Medium rectangle -->
<div class="banner" style="left:749px;top:282px;width:302px;height:250px;">
  <svg class="banner-band" viewBox="0 0 302 250" preserveAspectRatio="none" aria-hidden="true">
    <polygon points="0,194 302,142 302,250 0,250" fill="var(--tan)"/>
  </svg>
  <div class="brand-mark" style="left:39px;top:6px;width:40px;height:40px;"></div>
  <div class="brand-name" style="left:11px;top:54px;font-size:12.5px;">CLEARVIEW LEDGER</div>
  <div class="headline" style="left:11px;top:101px;font-size:25px;">WHAT WILL</div>
  <div class="headline" style="left:11px;top:118px;font-size:41px;">YOU DO</div>
  <div class="subline-box" style="left:11px;top:153px;width:136px;height:20px;font-size:10.5px;">WITH ALL THE CASH WE FIND YOU?</div>
  <div class="cta" style="left:11px;top:213px;width:94px;height:24px;font-size:10.5px;">LEARN MORE</div>
  <div class="mascot" role="img" aria-label="Cartoon finance mascot holding two bags of money" style="left:167px;top:42px;width:128px;height:196px;"></div>
</div>

<!-- Leaderboard large -->
<div class="banner" style="left:401px;top:554px;width:733px;height:90px;">
  <svg class="banner-band" viewBox="0 0 733 90" preserveAspectRatio="none" aria-hidden="true">
    <polygon points="571,0 733,0 733,90 590,90 606,45" fill="var(--tan)"/>
    <polygon points="606,45 590,90 612,90" fill="var(--tan-dark)"/>
  </svg>
  <div class="brand-mark" style="left:62px;top:6px;width:48px;height:48px;"></div>
  <div class="brand-name is-red center" style="left:10px;width:152px;top:65px;font-size:15px;">CLEARVIEW LEDGER</div>
  <div class="headline" style="left:215px;top:9px;font-size:35px;letter-spacing:2.4px;">WHAT WILL YOU DO</div>
  <div class="subline-box" style="left:215px;top:45px;width:318px;height:33px;font-size:22px;">WITH ALL THE CASH WE FIND YOU?</div>
  <div class="cta" style="left:625px;top:34px;width:98px;height:26px;font-size:11px;">LEARN MORE</div>
</div>

</body>
</html>
```